Einladungskarten-Design für Reinigung & Gebäudemangement
Zielgruppe:
Potentielle Kunden/Entscheider Einrichtungsleiter, Geschäftführer für den Bereich Alten- und Pflegeheime, Krankenhäuser.
Das Angebot geht über Verpflegungslösung, Reinigung, Gebäudemangement und Innovationen (z.B. zum Thema Digitalisierung, Roboting, .....).
Der Claim des Unternehmens ist 'Quality of Life Services = Services der Lebensqualität'
Aufgabenstellung
Gerne Pop-Up oder auch Relief - hochwertige Haptik von Umschlag und Karte ggf. Sonderformat d.h. nicht Standard DL quer
Sollte aber dennoch klassich gut wirken.
Die persönliche Note erhält die Karte durch handschriftliche Personalisierung durch den Sales Mitarbeiter.
Die Karte soll folgenden Text enthalten.
Text:
Das neue Jahr liegt vor Ihnen.
Nutzen Sie seine Chancen und ergreifen Sie seine Möglichkeiten.
Beispielsweise mit einem Gespräch
über inspierierende Ideen und neue Konzepte zur Steigerung der Lebensqualität
in Ihrem Hause.
Wir freuen uns mit Ihnen in Kontakt zu sein.
Der Umschlag soll Absenderadresse und Logo enthalten - dies wird nach Prämierung bekannt gegeben.
Natürlich kann auf der Rückseite der Karte auch das Logo mit Claim aufgedruckt werden.
Alle Bildrechte sollen nach Prämierung auf den Auftraggeber übergehen.

```html
<!DOCTYPE html>
<html lang="de">
<head>
<meta charset="utf-8">
<title>Neujahrskarten 2018</title>
<link href="https://fonts.googleapis.com/css2?family=Lato:wght@300;400&display=swap" rel="stylesheet">
<style>
  :root {
    --backdrop: #eef0f0;
    --paper: #ffffff;
    --text-light: #ffffff;
    --gold: #b8913f;
    --sky-rose: #e9d5de;
    --sky-lilac: #cfc6d8;
    --mist: #f2f1f3;
    --valley-blue: #3f6f8c;
    --valley-deep: #1d3445;
    --night: #0b1218;
    --sunset-high: #a9581a;
    --sunset-mid: #f39a2c;
    --sunset-glow: #f7b04a;
    --sunset-low: #d96f18;
    --hills: #3a2a20;
    --rock: #1a120c;
  }
  * { margin: 0; padding: 0; box-sizing: border-box; }
  html, body {
    width: 1200px; height: 908px; overflow: hidden;
    background: var(--backdrop);
    font-family: "Lato", sans-serif;
  }
  .stage {
    width: 1200px; height: 908px;
    display: flex; align-items: center; justify-content: center; gap: 40px;
  }
  .card {
    position: relative;
    width: 540px; height: 382px;
    overflow: hidden;
    background: var(--paper);
    box-shadow: 0 10px 30px rgba(0,0,0,0.12);
  }
  .card__photo { position: absolute; inset: 0; }
  .card__photo--clouds {
    background:
      radial-gradient(ellipse 55% 22% at 62% 62%, rgba(255,255,255,0.85), rgba(255,255,255,0) 70%),
      radial-gradient(ellipse 40% 16% at 35% 70%, rgba(235,240,245,0.6), rgba(235,240,245,0) 70%),
      radial-gradient(ellipse 45% 45% at 88% 82%, var(--night), rgba(11,18,24,0) 75%),
      linear-gradient(170deg, var(--sky-rose) 0%, var(--sky-lilac) 18%, var(--mist) 36%, var(--valley-blue) 55%, var(--valley-deep) 72%, var(--night) 92%);
  }
  .card__photo--sunset {
    background:
      radial-gradient(ellipse 60% 40% at 95% 95%, var(--rock), rgba(26,18,12,0) 80%),
      radial-gradient(ellipse 70% 12% at 40% 58%, var(--sunset-glow), rgba(247,176,74,0) 75%),
      linear-gradient(180deg, var(--sunset-high) 0%, var(--sunset-mid) 38%, var(--sunset-low) 60%, var(--hills) 70%, var(--rock) 82%, var(--rock) 100%);
  }
  .card__year { position: absolute; }
  .card__year text {
    font-family: "Lato", sans-serif; font-weight: 300;
    fill: none; stroke-width: 1.3;
  }
  .card--welcome .card__year { left: 36px; top: 214px; }
  .card--welcome .card__year text { stroke: var(--text-light); }
  .card__tagline {
    position: absolute; left: 40px; top: 304px;
    color: var(--text-light);
    font-weight: 300; font-size: 21px; letter-spacing: 0.2px;
  }
  .card__intro {
    position: absolute; left: 32px; top: 30px;
    padding: 30px 0 6px 14px;
    border-left: 2px solid var(--text-light);
    color: var(--text-light);
    font-weight: 300; font-size: 16px; line-height: 1.4;
  }
  .card--future .card__year { right: 26px; bottom: 22px; }
  .card--future .card__year text { stroke: var(--gold); }
</style>
</head>
<body>
  <main class="stage">
    <article class="card card--welcome">
      <div class="card__photo card__photo--clouds" role="img" aria-label="Foto: Wanderer mit Hut blickt bei Sonnenaufgang über ein Wolkenmeer zwischen Bergen"></div>
      <svg class="card__year" width="200" height="84" viewBox="0 0 200 84">
        <text x="0" y="72" font-size="78">2018</text>
      </svg>
      <p class="card__tagline">Ein neues Jahr erwartet Sie...</p>
    </article>

    <article class="card card--future">
      <div class="card__photo card__photo--sunset" role="img" aria-label="Foto: Läuferin springt als Silhouette vor orangem Abendhimmel über Felsen am Wasser"></div>
      <p class="card__intro">Das neue Jahr liegt<br>vor Ihnen.</p>
      <svg class="card__year" width="150" height="62" viewBox="0 0 150 62">
        <text x="0" y="54" font-size="60">2018</text>
      </svg>
    </article>
  </main>
</body>
</html>
```